IT Consulting Business Card Design

We need a business card on our company name....which is a IT consulting and staffing company. We also train masters graduates in various IT courses. 70% of the time these cards will be handed out to the graduate students at the universities. 30% for our clients and business partners. We are uploading our company logo...would like to see something that matches our logo or blends with it. Please visit www.brivolentaxis.com for more details on logo and colors.

Target Market(s)

70% of the time these cards will be handed out to the graduate students at the universities. 30% for our clients and business partners.

Industry/Entity Type

Business

Contact Information for Business Card

Tomas Verlinde
Vice-President
Brivolen Taxis Inc
3187 Corwick Lane, Suite 412
Eastbrook Falls, NJ 07099
tomas@brivolentaxis.com
Office : 1-855-555-0148 X 312
Cell number : 908-555-0193

Requirements
Nice to have
• may be company logo and name on the back of the card and detials on the other side...just a thought..!!

```html
<!DOCTYPE html>
<html lang="en">
<head>
<meta charset="utf-8">
<title>Brivolen Taxis – Business Card</title>
<link rel="stylesheet" href="https://fonts.googleapis.com/css2?family=PT+Sans:wght@400;700&family=Raleway:wght@400&display=swap">
<style>
  :root {
    --page-bg: #f2f2f2;
    --card-white: #ffffff;
    --card-white-low: #ececec;
    --ink: #2e2e2e;
    --ink-soft: #3a3a3a;
    --accent-red: #d7191f;
    --band-grey: #3b3b3b;
    --rule-grey: #9a9a9a;
    --back-dark-top: #3a3a3a;
    --back-dark-bottom: #1f1f1f;
    --back-text: #f4f4f4;
  }
  * { margin: 0; padding: 0; box-sizing: border-box; }
  html, body { width: 1200px; height: 900px; overflow: hidden; }
  body {
    background: var(--page-bg);
    font-family: "PT Sans", Arial, sans-serif;
    color: var(--ink);
    position: relative;
  }
  .card {
    position: absolute;
    top: 300px;
    width: 525px;
    height: 300px;
    border-radius: 22px;
    overflow: hidden;
    box-shadow: 0 10px 28px rgba(0,0,0,0.18);
  }
  /* Front */
  .card-front {
    left: 60px;
    background: linear-gradient(to bottom, var(--card-white) 0%, var(--card-white) 45%, var(--card-white-low) 100%);
  }
  .brand {
    position: absolute;
    left: 40px;
    top: 38px;
    display: flex;
    align-items: center;
    gap: 22px;
  }
  .brand-mark {
    width: 84px;
    height: 84px;
    border-radius: 50%;
    background: var(--accent-red);
  }
  .brand-name {
    font-family: "PT Sans", Arial, sans-serif;
    font-weight: 700;
    font-size: 38px;
    letter-spacing: 0.5px;
    color: var(--ink-soft);
  }
  .band {
    position: absolute;
    left: 0;
    top: 148px;
    width: 100%;
    height: 8px;
    background: var(--band-grey);
  }
  .person {
    position: absolute;
    left: 0;
    top: 190px;
    width: 178px;
    text-align: right;
  }
  .person-name {
    color: var(--accent-red);
    font-size: 17px;
    font-weight: 400;
  }
  .person-title {
    font-size: 11.5px;
    color: var(--ink);
    margin-top: 1px;
  }
  .divider {
    position: absolute;
    left: 192px;
    top: 180px;
    width: 1px;
    height: 95px;
    background: var(--rule-grey);
  }
  .contact-list {
    position: absolute;
    left: 206px;
    top: 181px;
    list-style: none;
    font-size: 16px;
    line-height: 19px;
    color: var(--ink);
  }
  .contact-list li { display: flex; align-items: flex-start; gap: 5px; }
  .contact-icon { width: 13px; height: 13px; flex: none; margin-top: 3px; }
  .contact-icon path, .contact-icon rect { fill: var(--accent-red); }
  .address-line { display: block; }
  /* Back */
  .card-back {
    left: 615px;
    background: linear-gradient(160deg, var(--back-dark-top) 0%, var(--back-dark-bottom) 100%);
  }
  .back-url {
    position: absolute;
    left: 0;
    right: 0;
    top: 138px;
    text-align: center;
    font-family: "Raleway", Arial, sans-serif;
    font-size: 21px;
    letter-spacing: 6.4px;
    color: var(--back-text);
  }
</style>
</head>
<body>
  <section class="card card-front" aria-label="Business card front">
    <div class="brand">
      <span class="brand-mark" aria-hidden="true"></span>
      <span class="brand-name">BRIVOLEN TAXIS</span>
    </div>
    <div class="band"></div>
    <div class="person">
      <p class="person-name">Tomas Verlinde</p>
      <p class="person-title">Vice-President</p>
    </div>
    <div class="divider"></div>
    <ul class="contact-list">
      <li>
        <svg class="contact-icon" viewBox="0 0 16 16" aria-hidden="true"><path d="M3.5 1l2.5 3.2-1.5 1.7c.9 2 2.6 3.7 4.6 4.6l1.7-1.5L14 11.5 12.6 14C6.7 13.6 2.4 9.3 2 3.4z"/></svg>
        <span>1-855-555-0148 X 312</span>
      </li>
      <li>
        <svg class="contact-icon" viewBox="0 0 16 16" aria-hidden="true"><path d="M4 1h8v14H4zM5.5 2.5v8h5v-8z"/></svg>
        <span>908-555-0193</span>
      </li>
      <li>
        <svg class="contact-icon" viewBox="0 0 16 16" aria-hidden="true"><path d="M1 3h14v10H1zM2.5 4.5L8 9l5.5-4.5z"/></svg>
        <span>tomas@brivolentaxis.com</span>
      </li>
      <li>
        <svg class="contact-icon" viewBox="0 0 16 16" aria-hidden="true"><path d="M8 1.5L1 8h2v6.5h4v-4h2v4h4V8h2z"/></svg>
        <span>
          <span class="address-line">3187 Corwick Lane,</span>
          <span class="address-line">Suite 412 Eastbrook Falls, NJ 07099</span>
        </span>
      </li>
    </ul>
  </section>

  <section class="card card-back" aria-label="Business card back">
    <p class="back-url">www.brivolentaxis.com</p>
  </section>
</body>
</html>
```